QUIET ORBIT/Invitational Figurative Show

I am having an open studio and have invited a number of artists to show one night only. I was thinking of cropping an image from each artist (just the heads of the figures ) and have a grid on the front of the card. I would like the information to be on the front as well as the back. The front could have a space at the bottom with all the info.
The back could have everyone's name (about 15 - could do just last names if we need space) as well as the address, show time, date email, web address and phone.
Also please add TEK to Maudie on the list of artists.

Industry/Entity Type

Artists

Font styles to use
Sans Serif

Colors
ec2027
fbd3d4
000000
757575

Requirements
Must have
• I must have the images in a white grid.

```html
<!DOCTYPE html>
<html lang="en">
<head>
<meta charset="utf-8">
<title>Quiet Orbit – Invitational Figurative Show</title>
<link rel="stylesheet" href="https://fonts.googleapis.com/css2?family=Jost:wght@300;400;600;700&display=swap">
<style>
  :root {
    --red: #ec2027;
    --pink: #fbd3d4;
    --black: #000000;
    --grey: #757575;
    --white: #ffffff;
    --ink: #1a1a1a;
  }
  * { margin: 0; padding: 0; box-sizing: border-box; }
  html, body { width: 1200px; height: 480px; overflow: hidden; background: var(--black); }
  body { position: relative; font-family: "Jost", "Futura", sans-serif; color: var(--ink); }

  /* Front card */
  .front-card {
    position: absolute; left: 40px; top: 20px; width: 560px; height: 435px;
    background: var(--grey);
  }
  .front-card__face {
    position: absolute; left: 60px; top: 0; width: 440px; height: 435px;
    background: var(--white);
  }
  .portrait-grid {
    position: absolute; left: 20px; top: 17px; width: 400px;
  }
  .portrait {
    position: absolute; width: 95px; height: 94px;
  }
  .front-title {
    position: absolute; left: 0; top: 320px; width: 100%;
    text-align: center; font-weight: 700; font-size: 38px; line-height: 1;
    letter-spacing: 0.5px; color: var(--black);
  }
  .front-subtitle {
    position: absolute; left: 0; top: 357px; width: 100%;
    text-align: center; font-weight: 300; font-size: 24px; line-height: 1;
    color: var(--black);
  }
  .date-band {
    position: absolute; left: 0; top: 385px; width: 100%; height: 16px;
    background: var(--red); color: var(--white);
    text-align: center; font-weight: 600; font-size: 11.5px; line-height: 16px;
    letter-spacing: 0.3px;
  }
  .front-contact {
    position: absolute; left: 0; top: 404px; width: 100%;
    text-align: center; font-size: 9px; line-height: 11px; color: var(--black);
  }

  /* Back card */
  .back-card {
    position: absolute; left: 613px; top: 20px; width: 559px; height: 435px;
    background: var(--white);
  }
  .title-block {
    position: absolute; left: 12px; top: 0; width: 258px; height: 77px;
    background: var(--red); color: var(--white); padding: 14px 0 0 10px;
  }
  .title-block__name { font-weight: 700; font-size: 27px; line-height: 1; letter-spacing: 0.3px; }
  .title-block__sub { font-weight: 400; font-size: 18px; line-height: 1; margin-top: 7px; }
  .event-info { position: absolute; left: 21px; top: 88px; color: var(--black); }
  .event-info__date { font-weight: 600; font-size: 18px; line-height: 1.1; margin-bottom: 3px; }
  .event-info__line { font-size: 13px; line-height: 16px; }
  .divider {
    position: absolute; left: 14px; top: 166px; width: 256px; height: 1px; background: var(--black);
  }
  .artist-list {
    position: absolute; top: 179px; list-style: none;
    font-size: 13px; line-height: 15.1px; color: var(--black);
  }
  .artist-list--first { left: 21px; }
  .artist-list--second { left: 139px; }
</style>
</head>
<body>

<section class="front-card">
  <div class="front-card__face">
    <div class="portrait-grid">
      <svg class="portrait" style="left:0;top:0" role="img" aria-label="Cropped head from a bronze figurative sculpture"><rect width="95" height="94" fill="#5a5f73"/></svg>
      <svg class="portrait" style="left:102px;top:0" role="img" aria-label="Cropped head from an abstract pastel figure"><defs><linearGradient id="g2" x1="0" y1="0" x2="1" y2="1"><stop offset="0" stop-color="#e9b36a"/><stop offset="1" stop-color="#8a6fb0"/></linearGradient></defs><rect width="95" height="94" fill="url(#g2)"/></svg>
      <svg class="portrait" style="left:203px;top:0" role="img" aria-label="Cropped head from a charcoal portrait"><rect width="95" height="94" fill="#6b6b6b"/></svg>
      <svg class="portrait" style="left:305px;top:0" role="img" aria-label="Cropped head from a blue ink figure drawing"><defs><linearGradient id="g4" x1="0" y1="0" x2="0" y2="1"><stop offset="0" stop-color="#8fc3e6"/><stop offset="1" stop-color="#dfeef7"/></linearGradient></defs><rect width="95" height="94" fill="url(#g4)"/></svg>

      <svg class="portrait" style="left:0;top:100px" role="img" aria-label="Cropped head from a pale blue painted figure"><defs><linearGradient id="g5" x1="0" y1="0" x2="1" y2="1"><stop offset="0" stop-color="#2b4d7a"/><stop offset="1" stop-color="#a8c0d8"/></linearGradient></defs><rect width="95" height="94" fill="url(#g5)"/></svg>
      <svg class="portrait" style="left:102px;top:100px" role="img" aria-label="Cropped head from a pencil sketch on cream paper"><rect width="95" height="94" fill="#e8e0c2"/></svg>
      <svg class="portrait" style="left:203px;top:100px" role="img" aria-label="Cropped head from a dark painting with green light"><defs><linearGradient id="g7" x1="0" y1="0" x2="0" y2="1"><stop offset="0" stop-color="#1c1c1c"/><stop offset="1" stop-color="#3c5a1e"/></linearGradient></defs><rect width="95" height="94" fill="url(#g7)"/></svg>
      <svg class="portrait" style="left:305px;top:100px" role="img" aria-label="Cropped head from an ink drawing of a reclining figure"><rect width="95" height="94" fill="#cfc8c0"/></svg>

      <svg class="portrait" style="left:102px;top:202px" role="img" aria-label="Cropped head from a colour illustration of a woman"><defs><linearGradient id="g9" x1="0" y1="0" x2="1" y2="1"><stop offset="0" stop-color="#3a2418"/><stop offset="1" stop-color="#b07a55"/></linearGradient></defs><rect width="95" height="94" fill="url(#g9)"/></svg>
      <svg class="portrait" style="left:203px;top:202px" role="img" aria-label="Cropped head from a purple painted figure"><defs><linearGradient id="g10" x1="0" y1="0" x2="1" y2="1"><stop offset="0" stop-color="#c79ab0"/><stop offset="1" stop-color="#5b4a7a"/></linearGradient></defs><rect width="95" height="94" fill="url(#g10)"/></svg>
      <svg class="portrait" style="left:305px;top:202px" role="img" aria-label="Cropped head from a graphite portrait study"><rect width="95" height="94" fill="#d9d1b8"/></svg>
    </div>

    <h1 class="front-title">QUIET ORBIT</h1>
    <p class="front-subtitle">Invitational Figurative Show</p>
    <p class="date-band">FRIDAY APRIL 10TH 5.PM TO 7.PM - ONE NIGHT ONLY</p>
    <p class="front-contact">STUDIO HALVERN, 2214 Larkin Street #41 (in back) Corvale, NM 87599<br>505 555-0142 | www.corvaleartist.us</p>
  </div>
</section>

<section class="back-card">
  <header class="title-block">
    <h2 class="title-block__name">QUIET ORBIT</h2>
    <p class="title-block__sub">Invitational Figurative Show</p>
  </header>
  <div class="event-info">
    <p class="event-info__date">FRIDAY APRIL 10TH 5 TO 7PM</p>
    <p class="event-info__line">STUDIO HALVERN 2214 Larkin Street #41</p>
    <p class="event-info__line">(in back) Corvale, NM 87599</p>
    <p class="event-info__line">505 555-0142 | www.corvaleartist.us</p>
  </div>
  <div class="divider"></div>
  <ul class="artist-list artist-list--first">
    <li>Omar Velin</li>
    <li>Andrea Halvern</li>
    <li>Anita Kessel</li>
    <li>Ann Pryor</li>
    <li>Maudie Tek</li>
    <li>Bob Fairley</li>
    <li>Clare Moyle</li>
    <li>Eric Dalby</li>
    <li>Erin Lasko</li>
    <li>George Tamsel</li>
  </ul>
  <ul class="artist-list artist-list--second">
    <li>Greta Vance</li>
    <li>Guy Pellam</li>
    <li>Holly Sarno</li>
    <li>Hye Lim</li>
    <li>John Averly</li>
    <li>Katie Halvern</li>
    <li>Corlissa</li>
    <li>Mathew Roan-Ellis</li>
    <li>Nita Ferrand</li>
    <li>Peter Olvey</li>
  </ul>
</section>

</body>
</html>
```